White Paper and One-Page Advertisement for TELVARIS-QP

I need both documents to be better formatted and designed so they look professional, not something someone with mediocre word skills put together. They will go out to 1000s of industry professionals, and they need to look sharp. I need them to have my company's color palate logo, and branding on it similar to how it is now, but better. Please do not change any of the written content, but it can be arranged in any other format you think is better. Smart art and things i've already used can be omitted in favor of better designs. The developer is free to use their creativity. White paper should not be longer than the three pages unless necessary.

Target Market(s)

Life Sciences supply chain professionals

Colors
33b8a4
0592cd
9bcb3c
fbee3e
3277b5

Requirements
Must have
• Must be professional looking and not look like something done in word. Please use the color palate as seen on the documents.
Should not have
• Any changes to the written content.

```html
<!DOCTYPE html>
<html lang="en">
<head>
<meta charset="utf-8">
<title>TELVARIS-QP White Paper – Page 3</title>
<link href="https://fonts.googleapis.com/css2?family=Barlow:ital,wght@0,400;0,600;0,700;1,600;1,700&family=Barlow+Condensed:wght@500;600;700&display=swap" rel="stylesheet">
<style>
:root{
  --page-bg:#dce7c5;
  --paper:#ffffff;
  --ink:#2b2b2b;
  --lime:#9bcb3c;
  --leaf:#8cbf3f;
  --olive:#bccf3c;
  --forest:#3a8f6c;
  --teal:#6aaeb1;
  --accent:#5a9a3a;
  --tint-lime:#eef3da;
  --tint-forest:#e4ebe4;
  --tint-teal:#e2ecee;
}
*{margin:0;padding:0;box-sizing:border-box}
html,body{width:846px;height:1200px;overflow:hidden}
body{background:var(--page-bg);font-family:"Barlow",Arial,sans-serif;color:var(--ink);position:relative;font-size:9.6px;line-height:13.2px}
.page-label{position:absolute;left:66px;top:29px;font-weight:700;font-size:13px;letter-spacing:.3px;font-family:"Barlow",sans-serif}
.side-strip{position:absolute;left:39px;top:70px;width:30px;height:1086px;background:linear-gradient(180deg,#c6dc93 0%,#9fbf85 40%,#4f8670 100%)}
.paper{position:absolute;left:69px;top:70px;width:737px;height:1086px;background:var(--paper)}
.col{position:absolute}
h2{font-family:"Barlow Condensed",sans-serif;font-weight:600;font-size:21px;line-height:22px;color:#222}
h3{font-family:"Barlow Condensed",sans-serif;font-weight:600;font-size:15.5px;line-height:18px;color:#222;margin-bottom:3px}
p{text-align:justify}
ul{list-style:none}
li{position:relative;padding-left:9px}
li::before{content:"";position:absolute;left:1px;top:5px;width:4px;height:4px;border-radius:50%;background:var(--lime)}
.justify li{text-align:justify}
.barrier{position:absolute;left:97px;width:326px}
.barrier .tab{display:inline-block;color:#fff;font-family:"Barlow Condensed",sans-serif;font-weight:600;font-size:15px;line-height:26px;padding:0 12px;float:left;margin:-6px 8px 0 0;height:26px}
.barrier .text{padding:6px 14px 3px 14px;text-align:justify}
.b-lime .tab{background:var(--leaf)} .b-lime{background:var(--tint-lime)}
.b-olive .tab{background:var(--olive)} .b-olive{background:var(--tint-lime)}
.b-forest .tab{background:var(--forest)} .b-forest{background:var(--tint-forest)}
.b-teal .tab{background:var(--teal)} .b-teal{background:var(--tint-teal)}
.vision{border-left:2px solid var(--lime);padding-left:6px;color:#6fae34;font-weight:700;font-style:italic;font-size:10.6px;line-height:13.8px;text-align:justify}
.hl{color:#3d8c6a;font-weight:700}
.sources p{text-align:left}
.sources .url{padding-left:26px;text-align:justify}
.sources .item{margin-bottom:9px}
.mark{position:absolute;left:640px;top:960px;width:160px;height:160px;opacity:.12}
.folio{position:absolute;left:766px;top:1121px;height:32px;border-left:2px solid var(--lime);padding-left:5px;font-weight:700;font-size:10px;line-height:14px}
</style>
</head>
<body>
<div class="page-label">PAGE 3</div>
<div class="side-strip"></div>
<div class="paper"></div>

<svg class="mark" viewBox="0 0 160 160" aria-hidden="true"><circle cx="80" cy="80" r="72" fill="none" stroke="#9bcb3c" stroke-width="10"/></svg>

<!-- Left column -->
<div class="col" style="left:97px;top:127px;width:326px">
  <h2>Refined Problem</h2>
  <p style="margin-top:4px">There is no clear market leader that helps organizations optimize waste, collaborative to reduce it, and market more quality materials to more firms whether for research, manufacturing, or donations. This marketplace must be regulated and all participates properly vetted and authenticated. Accounts must be created to enable companies to post materials and request for information/quotes. Additionally, this marketplace must facilitate collaborative relationships between companies that help them reduce supply chain costs. It must quickly, economically, compliantly, and legally facilitate those exchanges. Lack of this market leader may have enabled the waste problem as seen today.</p>
  <h3 style="margin-top:10px">Contemporary Operating Environment</h3>
  <ul class="justify" style="padding-left:24px">
    <li>Constant pressure from global competition, increasing customer and governmental demand on price, more regulatory scrutiny, and a relentless societal pursuit of sustainability are starting to erode what were once high margins for Pharma6.</li>
    <li>Regulators are cooperative and open to solutions.</li>
    <li>Exchanges and consortiums are not typically leveraged in Pharma.</li>
    <li>Pharma continues to struggle with the bullwhip effect.</li>
  </ul>
  <h3 style="margin-top:12px">Barriers</h3>
</div>

<div class="barrier b-lime" style="top:472px"><div class="text"><span class="tab">COMPLIANCE</span>It is the responsibility of manufacturers to provide customers/patients with quality, safe, and efficacious products. However, there is a misperception that high quality cGMP compliant materials, parts, and equipment cannot be sourced from aftermarket exchanges and consortiums.</div></div>
<div class="barrier b-olive" style="top:556px"><div class="text"><span class="tab">LIABILITY</span>Contractual agreements with suppliers have clauses to resolve issues dealing with poor quality. There is a misperception that these agreements cannot implemented at both the marketplace and transactionactional level.</div></div>
<div class="barrier b-forest" style="top:625px"><div class="text"><span class="tab">ECONOMICS</span>Exchanges can be difficult due to time/effort. A sanctioned marketplace can provide the structure to make it easy.</div></div>
<div class="barrier b-teal" style="top:683px"><div class="text"><span class="tab">SUSTAINABILITY</span>Firms have not discovered how to leverage exchanges to reduce environmental footprint and enable industry certifications as well as community trust.</div></div>
<div class="barrier b-lime" style="top:740px"><div class="text"><span class="tab">CONFIDENCE</span>Trust is critical to firms. They should know that a marketplace has properly vetted members with KPI data for analysis.</div></div>
<div class="barrier b-olive" style="top:796px"><div class="text"><span class="tab">SPEED</span>Exchanges should be fast. An innovative marketplace can ensure quick exchanges.</div></div>

<div class="col" style="left:97px;top:849px;width:326px">
  <h2>Root Cause &amp; Paradigm Shift</h2>
  <p style="margin-top:4px">Comfort in the status quo has enabled a culture of waste. With life science margins so high, it hasn't been a priority to solve. Additionally, there hasn't been an effective means to deal with waste. This limits the industry's ability to leverage these marketplaces. Finally, misperceived issues or liability and quality have strained innovation; all solvable problems.</p>
  <h3 style="margin-top:12px;margin-bottom:0">Future State</h3>
  <p>Creation of <span class="hl">Private Virtual Life Sciences Multi-Vendor Marketplace &amp; Consortium</span> where researchers, manufacturers, and original-end manufacturers can create a simple storefront for their organization and transact materials, equipment, parts, and collaborative relationships in a compliant and professional environment. This marketplace uses a series of software logic that leverages auditing capabilities of buyers and sellers by making FDA required data and documentation visible and subject to ALCOA-Plus, thus enabling transactions in a fast and compliant manner. This logic then automates contracts for digital signature in a part 11 compliant package.</p>
</div>

<!-- Right column -->
<div class="col" style="left:451px;top:127px;width:327px">
  <h3 style="font-size:16px">Benefits</h3>
  <ul style="padding-left:24px">
    <li>Avoid write-downs for surplus material/consumable stock</li>
    <li>Continue production when stocked-out of materials</li>
    <li>Reduce purchase price of materials</li>
    <li>Risk pool safety stock to reduce amount required</li>
    <li>Allow for leaner planning in that stock-outs can be addressed</li>
    <li>Allow for more responsive planning with an outlet to sell SS</li>
    <li>Reduce supplier audit resources and costs</li>
    <li>Reduce environment footprint by avoiding disposal fees</li>
  </ul>
  <h2 style="margin-top:8px">Vision</h2>
  <div class="vision" style="margin-top:6px">1. A collaborative and compliant multi-vendor marketplace is part of Pharma's normal operating practices .<br>2. Waste is not tolerated in the life sciences industry.<br>3. There is always a compliant outlet to procure and transact before and after market materials.</div>
  <h3 style="margin-top:18px">How to Implement</h3>
  <p>Application of the following guidance, regulations, and bodies will drive exchange process and design:</p>
  <ul class="justify" style="padding-left:24px;margin-top:3px">
    <li>ICH Q7 (international harmonized cGMP standards)</li>
    <li>CFR Title 21 (US cGMP standards)</li>
    <li>Data Integrity Draft Guidance by FDA (good doc practices)</li>
    <li>WHO GMP for Pharmaceutical Products (World Health Organizations cGMP standards)</li>
    <li>APIC - Good Manufacturing Practices in Active Pharmaceutical</li>
    <li>Ingredients Development, 1999.</li>
    <li>APIC Supplier Qualification and Management Guidelines</li>
  </ul>
  <h3 style="margin-top:12px">Data Integrity</h3>
  <p>Data integrity will drive how the exchange operates. All parties are encouraged to use the FDA's ALCOA-Plus system to review documents associated with transactions. This enables buyers' standards of data integrity and cGMP quality compliance to be adhered.</p>
  <h3 style="margin-top:16px">How to Find Out More</h3>
  <p>The exciting new marketplace called TELVARIS-QP is scheduled for initial launch 03 November 2018.</p>
  <div style="padding-left:34px;margin-top:7px">
    <div style="font-weight:600">For more information:</div>
    <ul>
      <li>Email Dana Marlow</li>
      <li>Visit www.telvarisqp.com</li>
      <li>Call 844-555-TVQP</li>
    </ul>
  </div>
  <p style="margin-top:10px"><b>*WE</b> enable a greener, more cost-efficient, and quality driven supply chain through a collaborative life sciences marketplace.</p>
  <p style="margin-top:13px"><b>*WE</b> are an emerging small business with the ultimate goal to educate, inspire, and align Pharma around a new paradigm of waste optimization and sourcing strategies.</p>
  <p style="margin-top:13px"><b>*WE</b> aspire to increase medicine access around the world and decrease Pharma's overall environmental impact</p>
  <h3 style="margin-top:12px">Sources</h3>
  <div class="sources">
    <div class="item"><p>1. Top 100 Pharma Companies</p><p class="url">https://reports.pharmaledger-example.com/-/media/marketing/top-100/pdf/Top100_LeagueTables.pdf?la=en</p></div>
    <div class="item"><p>2. 2016 Annual/10K Reports</p><p class="url">Avelon, Brightmoor, Corvana, Delphion, Estrava, Fennix, Galvora, Halcyra, Istrel, Jovane, Kestral, Lumora, Medrion, Novelle, Orvana, Pellix, Quorra, Rennet</p></div>
    <div class="item"><p>3. Total Pharma Revenue 2016</p><p class="url">http://journals.chemfield-example.org/doi/pdfplus/10.1021/chemneuro.7b00253</p></div>
    <div class="item"><p>4. Currency Exchange Rates 29 Jan 2018</p><p class="url">http://www.fxtables-example.com/table/?from=USD&amp;amount=1</p></div>
    <div class="item"><p>5. Pricing Pressure</p><p class="url">http://www.medjournal-example.org/doi/full/10.1056/MJp160129</p></div>
  </div>
</div>

<div class="folio">2</div>
</body>
</html>
```